会社の名刺デザインを作成お願いいたします。
新しい企業のため、信頼感、高級感、親しみやすさ、ロゴとの相性などを
見ていきたいと思います。
名刺の背景は白地となります。
記載項目
表面:ロゴ/株式会社晴嶺クラフトネット/企画部部長/佐伯春樹/〒222-2222 東京都港区白金○○○/03-5555-5555/03-5555-5555/ saeki@seireicraft.jp

裏面:事業内容: こちらは枠だけでお願いします。
お任せします。 ロゴが活きるデザインをお願いいたします。
ロゴのファイルをアップいたしました。
依頼金額を上げました。
よろしくお願いいたします。
納品形式は、イラストレーター形式ですが、
こちらで内容を修正しますので、アウトラインをかけたものと、
かけていない物両パターンの納品をお願いいたします。
数々のご提案ありがとうございます。
素敵な作品が多くびっくりしました。

残り一日ですが、ロゴに合せると難しいとは思いますが、
健康になりそうな、爽やかなイメージにもできますか?
よろしくお願いいたします。
新しい配色のロゴをアップしました。
爽やかな名刺をお待ちしております。
ロゴはもう少し小さく配置して頂いてもいいかもしれません。

一日だけ締め切りを延長いたしました。
どうぞよろしくお願いいたします。

見たこともない斬新なアイディア、イラストに感動しました。

皆様ありがとうございました。
少ない情報を活かし、アイディアを出していただいた事、
この場を借りてお礼申し上げます。
皆様を当選に選びたいくらいの気持ちです。
今後ともよろしくお願いいたします!

```html
<!DOCTYPE html>
<html lang="ja">
<head>
<meta charset="utf-8">
<title>名刺デザイン 表面 3案</title>
<link rel="stylesheet" href="https://fonts.googleapis.com/css2?family=Noto+Sans+JP:wght@400;700&display=swap">
<style>
  :root {
    --paper: #ffffff;
    --ink: #1a1a1a;
    --sub-ink: #555555;
    --trim: #333333;
    --card-edge: #222222;
    --accent-green: #3f9b3a;
    --accent-red: #d8332c;
    --accent-yellow: #e6b81e;
  }
  * { box-sizing: border-box; margin: 0; padding: 0; }
  html, body { width: 849px; height: 1200px; overflow: hidden; background: var(--paper); }
  body { position: relative; font-family: "Noto Sans JP", sans-serif; color: var(--ink); }

  .card-sheet { position: absolute; width: 540px; height: 318px; }
  .card-sheet--horizontal { left: 148px; top: 52px; }
  .card-sheet--stacked { left: 160px; top: 455px; }
  .card-sheet--footer-logo { left: 128px; top: 860px; }

  .trim-marks { position: absolute; left: -30px; top: -30px; width: 600px; height: 378px; }
  .trim-marks line { stroke: var(--trim); stroke-width: 0.8; }

  .card { position: absolute; inset: 0; background: var(--paper); border: 1.2px solid var(--card-edge); }

  .brand-name { position: absolute; font-weight: 700; color: var(--ink); letter-spacing: 0.02em; line-height: 1.05; white-space: nowrap; }
  .brand-name .line { display: block; }
  .brand-url { position: absolute; font-size: 9px; color: var(--ink); letter-spacing: 0.05em; white-space: nowrap; }

  .company { position: absolute; font-size: 14px; font-weight: 700; letter-spacing: 0.02em; white-space: nowrap; }
  .person { position: absolute; font-size: 10px; white-space: nowrap; }
  .person .name { font-size: 15px; font-weight: 700; margin-left: 14px; letter-spacing: 0.2em; }

  .contact { position: absolute; list-style: none; font-size: 8.5px; line-height: 1.55; color: var(--sub-ink); white-space: nowrap; }
  .contact li { display: flex; align-items: center; gap: 5px; }
  .contact .dot { width: 6px; height: 6px; flex: none; }
  .dot--green { background: var(--accent-green); }
  .dot--red { background: var(--accent-red); }
  .dot--yellow { background: var(--accent-yellow); }

  /* 案1 */
  .card-sheet--horizontal .brand-name { left: 0; right: 0; top: 38px; text-align: center; font-size: 60px; }
  .card-sheet--horizontal .company { left: 48px; top: 172px; }
  .card-sheet--horizontal .person { left: 48px; top: 198px; }
  .card-sheet--horizontal .contact { left: 48px; top: 228px; }

  /* 案2 */
  .card-sheet--stacked .brand-name { left: 38px; top: 40px; font-size: 44px; }
  .card-sheet--stacked .brand-url { left: 42px; top: 150px; }
  .card-sheet--stacked .company { left: 236px; top: 74px; }
  .card-sheet--stacked .person { left: 236px; top: 100px; }
  .card-sheet--stacked .contact { left: 236px; top: 130px; }

  /* 案3 */
  .card-sheet--footer-logo .company { left: 38px; top: 40px; }
  .card-sheet--footer-logo .person { left: 38px; top: 66px; }
  .card-sheet--footer-logo .contact { left: 300px; top: 42px; }
  .card-sheet--footer-logo .brand-name { left: 38px; top: 168px; font-size: 62px; }
  .card-sheet--footer-logo .brand-url { left: 42px; top: 262px; }

  .side-label { position: absolute; left: 694px; top: 892px; font-size: 66px; font-weight: 400; line-height: 1; }
  .print-note { position: absolute; left: 676px; top: 985px; width: 150px; font-size: 11px; line-height: 1.75; color: var(--ink); }
</style>
</head>
<body>

  <section class="card-sheet card-sheet--horizontal" aria-label="名刺 案1">
    <svg class="trim-marks" viewBox="0 0 600 378" aria-hidden="true">
      <line x1="20" y1="0" x2="20" y2="22"/><line x1="30" y1="0" x2="30" y2="22"/>
      <line x1="0" y1="20" x2="22" y2="20"/><line x1="0" y1="30" x2="22" y2="30"/>
      <line x1="580" y1="0" x2="580" y2="22"/><line x1="570" y1="0" x2="570" y2="22"/>
      <line x1="600" y1="20" x2="578" y2="20"/><line x1="600" y1="30" x2="578" y2="30"/>
      <line x1="20" y1="378" x2="20" y2="356"/><line x1="30" y1="378" x2="30" y2="356"/>
      <line x1="0" y1="358" x2="22" y2="358"/><line x1="0" y1="348" x2="22" y2="348"/>
      <line x1="580" y1="378" x2="580" y2="356"/><line x1="570" y1="378" x2="570" y2="356"/>
      <line x1="600" y1="358" x2="578" y2="358"/><line x1="600" y1="348" x2="578" y2="348"/>
      <line x1="300" y1="0" x2="300" y2="20"/><line x1="300" y1="358" x2="300" y2="378"/>
      <line x1="0" y1="189" x2="20" y2="189"/><line x1="580" y1="189" x2="600" y2="189"/>
    </svg>
    <div class="card">
      <p class="brand-name">晴嶺クラフト</p>
      <p class="company">株式会社晴嶺クラフトネット</p>
      <p class="person">企画部部長<span class="name">佐伯 春樹</span></p>
      <ul class="contact">
        <li><span class="dot dot--green"></span>〒222-2222</li>
        <li><span class="dot dot--green"></span>東京都港区白金○○○</li>
        <li><span class="dot dot--red"></span>03-5555-5555</li>
        <li><span class="dot dot--yellow"></span>03-5555-5555</li>
        <li><span class="dot dot--yellow"></span>saeki@seireicraft.jp</li>
      </ul>
    </div>
  </section>

  <section class="card-sheet card-sheet--stacked" aria-label="名刺 案2">
    <svg class="trim-marks" viewBox="0 0 600 378" aria-hidden="true">
      <line x1="20" y1="0" x2="20" y2="22"/><line x1="30" y1="0" x2="30" y2="22"/>
      <line x1="0" y1="20" x2="22" y2="20"/><line x1="0" y1="30" x2="22" y2="30"/>
      <line x1="580" y1="0" x2="580" y2="22"/><line x1="570" y1="0" x2="570" y2="22"/>
      <line x1="600" y1="20" x2="578" y2="20"/><line x1="600" y1="30" x2="578" y2="30"/>
      <line x1="20" y1="378" x2="20" y2="356"/><line x1="30" y1="378" x2="30" y2="356"/>
      <line x1="0" y1="358" x2="22" y2="358"/><line x1="0" y1="348" x2="22" y2="348"/>
      <line x1="580" y1="378" x2="580" y2="356"/><line x1="570" y1="378" x2="570" y2="356"/>
      <line x1="600" y1="358" x2="578" y2="358"/><line x1="600" y1="348" x2="578" y2="348"/>
      <line x1="300" y1="0" x2="300" y2="20"/><line x1="300" y1="358" x2="300" y2="378"/>
      <line x1="0" y1="189" x2="20" y2="189"/><line x1="580" y1="189" x2="600" y2="189"/>
    </svg>
    <div class="card">
      <p class="brand-name"><span class="line">晴嶺</span><span class="line">クラフト</span></p>
      <p class="brand-url">seireicraft.jp</p>
      <p class="company">株式会社晴嶺クラフトネット</p>
      <p class="person">企画部部長<span class="name">佐伯 春樹</span></p>
      <ul class="contact">
        <li><span class="dot dot--green"></span>〒222-2222</li>
        <li><span class="dot dot--green"></span>東京都港区白金○○○</li>
        <li><span class="dot dot--red"></span>03-5555-5555</li>
        <li><span class="dot dot--yellow"></span>03-5555-5555</li>
        <li><span class="dot dot--yellow"></span>saeki@seireicraft.jp</li>
      </ul>
    </div>
  </section>

  <section class="card-sheet card-sheet--footer-logo" aria-label="名刺 案3">
    <svg class="trim-marks" viewBox="0 0 600 378" aria-hidden="true">
      <line x1="20" y1="0" x2="20" y2="22"/><line x1="30" y1="0" x2="30" y2="22"/>
      <line x1="0" y1="20" x2="22" y2="20"/><line x1="0" y1="30" x2="22" y2="30"/>
      <line x1="580" y1="0" x2="580" y2="22"/><line x1="570" y1="0" x2="570" y2="22"/>
      <line x1="600" y1="20" x2="578" y2="20"/><line x1="600" y1="30" x2="578" y2="30"/>
      <line x1="20" y1="378" x2="20" y2="356"/><line x1="30" y1="378" x2="30" y2="356"/>
      <line x1="0" y1="358" x2="22" y2="358"/><line x1="0" y1="348" x2="22" y2="348"/>
      <line x1="580" y1="378" x2="580" y2="356"/><line x1="570" y1="378" x2="570" y2="356"/>
      <line x1="600" y1="358" x2="578" y2="358"/><line x1="600" y1="348" x2="578" y2="348"/>
      <line x1="300" y1="0" x2="300" y2="20"/><line x1="300" y1="358" x2="300" y2="378"/>
      <line x1="0" y1="189" x2="20" y2="189"/><line x1="580" y1="189" x2="600" y2="189"/>
    </svg>
    <div class="card">
      <p class="company">株式会社晴嶺クラフトネット</p>
      <p class="person">企画部部長<span class="name">佐伯 春樹</span></p>
      <ul class="contact">
        <li><span class="dot dot--green"></span>〒222-2222</li>
        <li><span class="dot dot--green"></span>東京都港区白金○○○</li>
        <li><span class="dot dot--red"></span>03-5555-5555</li>
        <li><span class="dot dot--yellow"></span>03-5555-5555</li>
        <li><span class="dot dot--yellow"></span>saeki@seireicraft.jp</li>
        <li><span class="dot dot--yellow"></span>www.seireicraft.jp</li>
      </ul>
      <p class="brand-name">晴嶺クラフト</p>
      <p class="brand-url">seireicraft.jp</p>
    </div>
  </section>

  <p class="side-label">表</p>
  <p class="print-note">※名刺の黒枠は大きさを表すためにつけています。印刷するときは黒枠を消して印刷して下さい。</p>

</body>
</html>
```